Long Established Local Fencing (not swords) Business needs fresh Business Cards

We need fresh double sided business cards for our Fencing Construction business, we are looking for something with our new logo design added, and maybe a photo background ?
We recently had cards made from Cardlyne and we were horrified with what we got back, the quality was terrible, so am looking for high quality format for good printing company to make.
We install Steelmora, Timber paling, Aluminium Slat Screening, Picket (timber and aluminium) and most other fencing installations.
Our website is brankelrails.com.au should you like to learn a bit more.
We do have logo in other formats if required.
We have been in business for over 35 years and we have used this as a "motto" it is on our signage

Industry/Entity Type

Construction

Contact Information for Business Card

Open to ideas, we need 3 x different cards, one generic with no name and 2 x others each with 1 of our bosses name on each, I will put into upload files.

Colors
ec1f27
000000
606060
f5f5f5

Requirements
Must have
• Company Name and Logo
• Address
• Contact details, phone, website, email etc
• Small space to write notes when leaving card at residence
Nice to have
• Our motto "Servicing the Peninsula for over 35 years"

```html
<!DOCTYPE html>
<html lang="en">
<head>
<meta charset="utf-8">
<title>Brankel Rails – Business Cards</title>
<link rel="stylesheet" href="https://fonts.googleapis.com/css2?family=Ubuntu:wght@400;500;700&display=swap">
<style>
  :root {
    --brand-red: #dc3232;
    --brand-black: #141516;
    --brand-grey: #606060;
    --card-white: #f3f3f3;
    --stage: #8c8c8c;
    --ink: #1d1d1d;
  }
  * { margin: 0; padding: 0; box-sizing: border-box; }
  html, body { width: 1200px; height: 1200px; overflow: hidden; }
  body {
    background: var(--stage);
    position: relative;
    font-family: "Ubuntu", sans-serif;
  }
  .card {
    position: absolute;
    top: 310px;
    height: 594px;
    border-radius: 16px;
    overflow: hidden;
  }
  .card-front {
    left: 234px;
    width: 363px;
    background: var(--card-white);
    text-align: center;
    color: var(--ink);
  }
  .card-back {
    left: 627px;
    width: 370px;
    background: linear-gradient(to bottom, var(--brand-black) 0 55%, var(--brand-red) 55% 100%);
    color: #fff;
    text-align: center;
  }
  .brand-mark {
    position: absolute;
    left: 50%;
    transform: translateX(-50%);
    border-radius: 50%;
  }
  .card-front .brand-mark {
    top: 80px;
    width: 96px;
    height: 96px;
    background: var(--brand-red);
  }
  .brand-name {
    position: absolute;
    left: 0; right: 0;
    font-weight: 700;
    letter-spacing: 2px;
  }
  .card-front .brand-name {
    top: 210px;
    font-size: 40px;
    line-height: 46px;
    color: var(--brand-black);
  }
  .person {
    position: absolute;
    top: 396px;
    left: 0; right: 0;
  }
  .person-name {
    color: var(--brand-red);
    font-weight: 700;
    font-size: 19px;
    letter-spacing: 0.3px;
  }
  .person-role {
    font-size: 16px;
    margin-top: 1px;
  }
  .contact-divider {
    position: absolute;
    top: 460px;
    left: 88px;
    width: 188px;
    height: 22px;
  }
  .contact-list {
    position: absolute;
    top: 487px;
    left: 0; right: 0;
    font-size: 16px;
    line-height: 22px;
    list-style: none;
  }
  .card-back .brand-mark {
    top: 150px;
    width: 150px;
    height: 150px;
    background: var(--brand-red);
  }
  .card-back .brand-name {
    top: 340px;
    font-size: 44px;
    line-height: 50px;
    color: #fff;
  }
  .motto {
    position: absolute;
    top: 505px;
    left: 0; right: 0;
    font-size: 18px;
    line-height: 29px;
    letter-spacing: 0.3px;
  }
</style>
</head>
<body>
  <section class="card card-front">
    <div class="brand-mark"></div>
    <div class="brand-name">BRANKEL<br>RAILS</div>
    <div class="person">
      <p class="person-name">MARCUS HALE</p>
      <p class="person-role">Managing Director</p>
    </div>
    <svg class="contact-divider" viewBox="0 0 188 22" aria-hidden="true">
      <line x1="0" y1="11" x2="58" y2="11" stroke="#888" stroke-width="1"/>
      <line x1="130" y1="11" x2="188" y2="11" stroke="#888" stroke-width="1"/>
      <circle cx="71" cy="11" r="10" fill="#dc3232"/>
      <path d="M66.5 6.5c.8-.8 1.6-.5 2 .3l.8 1.6c.3.6 0 1.1-.5 1.5.6 1.3 1.5 2.2 2.8 2.8.4-.5.9-.8 1.5-.5l1.6.8c.8.4 1.1 1.2.3 2-1 1-2.6 1.2-4.6-.2-1.9-1.3-3.3-2.8-4.3-4.6-.8-1.6-.6-2.7.4-3.7z" fill="#fff"/>
      <circle cx="94" cy="11" r="10" fill="#dc3232"/>
      <rect x="88.5" y="7.5" width="11" height="7.5" rx="1" fill="#fff"/>
      <path d="M88.8 8l5.2 4 5.2-4" stroke="#dc3232" stroke-width="1" fill="none"/>
      <circle cx="117" cy="11" r="10" fill="#dc3232"/>
      <circle cx="117" cy="11" r="5.5" fill="none" stroke="#fff" stroke-width="1.4"/>
      <path d="M111.5 11h11M117 5.5c-2.5 3-2.5 8 0 11M117 5.5c2.5 3 2.5 8 0 11" stroke="#fff" stroke-width="1" fill="none"/>
    </svg>
    <ul class="contact-list">
      <li>444 555 6688</li>
      <li>info@youremail.com</li>
      <li>www.websitename.com</li>
    </ul>
  </section>

  <section class="card card-back">
    <div class="brand-mark"></div>
    <div class="brand-name">BRANKEL<br>RAILS</div>
    <p class="motto">SERVICING THE PENINSULA<br>FOR OVER 35 YEARS</p>
  </section>
</body>
</html>
```